French Puns

Creation of a cover for a book on French plays on words.
The public is lovers of the French language
TITLE: The gentle phrases of Honoré Vasseline
SUB-TITLE: Witty words, wit of words
PUBLISHER (at the bottom of the page): Editions Plumeau
(See joined examples, previous books of the same author)
Size: 14 x 20.5 cm
Please note that the text on the cover is in French, not in English:
Fine phrases from Honoré Vasseline
Witty words, witty words (subtitle, smaller)
Plumeau Editions

```html
<!DOCTYPE html>
<html lang="en">
<head>
<meta charset="utf-8">
<title>The gentle phrases of Honoré Vasseline — cover</title>
<link rel="stylesheet" href="https://fonts.googleapis.com/css2?family=Federo&family=Cinzel:wght@400;500&display=swap">
<style>
  :root {
    --stage: #e9eef0;
    --paper: #ffffff;
    --ink-navy: #20206a;
    --ink-red: #d61a3c;
    --flag-red: #c81f2e;
    --flag-blue: #2f3d94;
    --flag-white: #f4f4f4;
    --shade: #c9c9cc;
  }
  * { margin: 0; padding: 0; box-sizing: border-box; }
  html, body {
    width: 1200px; height: 800px; overflow: hidden;
    background: var(--stage);
  }
  .canvas {
    width: 1200px; height: 800px;
    display: flex; align-items: center; justify-content: center;
  }
  .cover {
    position: relative;
    width: 500px; height: 732px;
    background: var(--paper);
    box-shadow: 0 6px 24px rgba(0,0,0,0.12);
    display: flex; flex-direction: column; align-items: center;
    padding: 40px 30px 34px;
  }
  .title {
    font-family: "Federo", sans-serif;
    color: var(--ink-navy);
    text-align: center;
    font-weight: 400;
    line-height: 1;
  }
  .title__lead { display: block; font-size: 52px; font-variant: small-caps; }
  .title__middle { display: block; font-size: 46px; margin-top: 34px; text-transform: uppercase; letter-spacing: 0.5px; }
  .title__author {
    display: flex; align-items: flex-end; justify-content: center;
    margin-top: 22px;
    font-family: "Cinzel", serif;
    font-size: 32px; letter-spacing: 7px; text-transform: uppercase;
  }
  .author-ornament {
    width: 42px; height: 86px; margin-right: 8px;
    background: linear-gradient(180deg, #5a5a95, var(--ink-navy));
    clip-path: polygon(48% 0, 52% 0, 100% 100%, 0 100%);
  }
  .subtitle {
    margin-top: 46px;
    font-family: "Cinzel", serif;
    font-size: 23px; letter-spacing: 2px;
    font-variant: small-caps;
    color: var(--ink-red);
  }
  .mascot {
    margin-top: 40px;
    width: 380px; height: 300px;
    border-radius: 18px;
    background: linear-gradient(90deg, var(--flag-red) 0 33%, var(--flag-white) 33% 66%, var(--flag-blue) 66% 100%);
    opacity: 0.9;
  }
  .publisher {
    margin-top: auto;
    font-family: "Federo", sans-serif;
    font-size: 31px;
    color: var(--ink-red);
    white-space: nowrap;
  }
  .publisher__name { font-variant: small-caps; }
</style>
</head>
<body>
  <main class="canvas">
    <section class="cover">
      <h1 class="title">
        <span class="title__lead">The</span>
        <span class="title__middle">gentle phrases of</span>
        <span class="title__author">
          <span class="author-ornament" role="img" aria-label="Small navy Eiffel Tower ornament"></span>
          Honoré Vasseline
        </span>
      </h1>
      <p class="subtitle">Witty words, wit of words</p>
      <div class="mascot" role="img" aria-label="Cartoon French flag mascot in a clown hat waving with both hands"></div>
      <p class="publisher">PUBLISHER: <span class="publisher__name">Editions Plumeau</span></p>
    </section>
  </main>
</body>
</html>
```